Non fiction leadership Book Cover design needed for “Hold Fast: Forge A Steady Track”

I need a front cover design for a new book 6 X 9 traditional non-fiction book.

Title: "Hold FAST - Forge A Steady Track"

The subtitle is not finalized- so use 2 lines of smaller dummy text

My brand guide is attached (please use the tan color sparingly)

I'd like to see FAST look like it is in motion and "flying" across the page

Need CREATIVE designs and options

Do not want my picture on the front cover - I do want it on the back cover.

On the front cover I’d like to see creative use of font to create movement on “FAST”

Target Market(s)

Business leaders

Industry/Entity Type

Aviation

Font styles to use
Other font styles liked:
• See style guide- can add additional font (modern script or san serif)

Colors
0054AA
0677BA
7BADD7
CADEEF
E8F1F8
EB3D1F
EC4F4E
F09395
F8D3D4
FCEDEE

Requirements
Must have
• Creative font use, using perspective to create movement/motion on FAST
Should not have
• My picture on the front cover- my picture should be on the back cover

```html
<!DOCTYPE html>
<html lang="en">
<head>
<meta charset="utf-8">
<title>Hold Fast: Forge A Steady Track — Front Cover</title>
<link rel="stylesheet" href="https://fonts.googleapis.com/css2?family=Teko:wght@500;600&family=Inter:wght@400&display=swap">
<style>
  :root {
    --stage: #ececec;
    --teal: #3fb3b4;
    --teal-deep: #2f7f8c;
    --navy: #2c4d6e;
    --sky: #9fd3cc;
    --sun: #f3c777;
    --amber: #f0a25a;
    --coral: #e9604e;
    --red: #e2453c;
    --tan: #ecd3b2;
    --white: #ffffff;
  }
  * { margin: 0; padding: 0; box-sizing: border-box; }
  html, body {
    width: 1200px;
    height: 960px;
    overflow: hidden;
    background: var(--stage);
  }
  .canvas {
    position: relative;
    width: 1200px;
    height: 960px;
  }
  .book-cover {
    position: absolute;
    left: 330px;
    top: 30px;
    width: 540px;
    height: 900px;
    overflow: hidden;
    background: var(--teal);
  }
  .cover-art {
    position: absolute;
    inset: 0;
    background:
      radial-gradient(ellipse 45% 28% at 28% 20%, rgba(240,120,80,0.85), transparent 70%),
      radial-gradient(ellipse 55% 32% at 68% 45%, rgba(243,199,119,0.95), transparent 75%),
      radial-gradient(ellipse 60% 45% at 85% 85%, var(--red), transparent 80%),
      linear-gradient(90deg, var(--navy) 0%, var(--teal-deep) 45%, var(--coral) 52%, var(--red) 100%);
  }
  .cover-art::before {
    content: "";
    position: absolute;
    inset: 0 0 45% 0;
    background: linear-gradient(180deg, var(--teal) 0%, var(--sky) 40%, transparent 100%);
    opacity: 0.55;
  }
  .cover-text {
    position: absolute;
    left: 0;
    right: 0;
    top: 505px;
    text-align: center;
  }
  .title-main {
    display: flex;
    justify-content: center;
    align-items: baseline;
    gap: 22px;
    white-space: nowrap;
    font-family: "Teko", sans-serif;
    font-weight: 600;
    font-size: 124px;
    line-height: 0.8;
    letter-spacing: 1px;
    color: var(--tan);
  }
  .title-fast {
    position: relative;
    display: inline-block;
    transform-origin: left center;
    transform: perspective(520px) rotateY(-24deg) skewX(-12deg);
  }
  .speed-lines {
    position: absolute;
    left: -58px;
    top: 14px;
    width: 56px;
    height: 70px;
  }
  .title-sub {
    font-family: "Teko", sans-serif;
    font-weight: 500;
    font-size: 46px;
    line-height: 1;
    letter-spacing: 1px;
    color: var(--tan);
    margin-top: 14px;
    white-space: nowrap;
  }
  .subtitle {
    font-family: "Inter", sans-serif;
    font-weight: 400;
    font-size: 16px;
    line-height: 1.45;
    color: var(--white);
    margin-top: 16px;
  }
</style>
</head>
<body>
  <div class="canvas">
    <section class="book-cover">
      <div class="cover-art" role="img" aria-label="Painted illustration: a lone figure standing on a tall cliff peak against glowing teal, orange and red clouds"></div>
      <div class="cover-text">
        <h1 class="title-main">
          <span class="title-hold">HOLD</span>
          <span class="title-fast">
            <svg class="speed-lines" viewBox="0 0 56 70" aria-hidden="true">
              <line x1="6" y1="12" x2="54" y2="12" stroke="#ecd3b2" stroke-width="4" stroke-linecap="round" opacity="0.55"/>
              <line x1="18" y1="34" x2="54" y2="34" stroke="#ecd3b2" stroke-width="4" stroke-linecap="round" opacity="0.75"/>
              <line x1="0" y1="56" x2="54" y2="56" stroke="#ecd3b2" stroke-width="4" stroke-linecap="round" opacity="0.4"/>
            </svg>FAST</span>
        </h1>
        <p class="title-sub">FORGE A STEADY TRACK</p>
        <p class="subtitle">Beginner Principles, Strategies, and<br>Exercises to Outmaneuver Opponents.</p>
      </div>
    </section>
  </div>
</body>
</html>
```